Facebook Cover & Profile Branding for VelbrooK Systems

We need a modern, premium Facebook cover image for our company Velbrook Systems GmbH. The design should be clean, professional, and aligned with our corporate colors (neon green and deep blue) as well as our logo. It should clearly represent us as a technology and IT consulting company with a strong focus on software testing and quality assurance.

Since Velbrook Systems is also active in the U.S. market, the design may include global or U.S.-related elements (e.g., subtle references to international presence, tech innovation with a global reach).

Requirements:

Integration of the Velbrook logo and brand colors

Modern, premium look with a tech-driven feel

Clear, simple layout that looks good on desktop and mobile

Optional: subtle U.S./international references to highlight our global presence

Goal:
A professional, eye-catching Facebook cover image that strengthens our brand identity and reflects our international expansion into the U.S. market.

Target Market(s)

Medium to large enterprises in the technology, finance, and energy sectors - Companies looking for premium IT consulting, software testing, and quality assurance services - Decision makers and executives (CIOs, CTOs, IT managers) in Europe and the United States - A global audience that values innovation, professionalism, and trust

Industry/Entity Type

Information Technology & Consulting Software Testing & Quality Assurance Technology / Professional Services Global IT Consulting with U.S. Market Presence

Requirements
Must have
• Integration of the Velbrook Systems logo and brand colors (Neon Green & Deep Blue) Modern, premium design with a strong tech-oriented look and feel Clean and professional layout, optimized for both desktop and mobile display Clear visibility of the brand identity (technology, IT consulting, software testing, quality assurance) Subtle reference to U.S. presence / global expansion (to highlight activity in both Germany and the U.S.) Balanced use of colors and space for a high-end, corporate appearance
Nice to have
• Subtle animations or motion effects (e.g., light gradients, moving lines, glowing accents) Dark/Light version option for different moods or seasonal campaigns Integration of social media icons (LinkedIn, Instagram, Facebook) in a clean, minimal way Tech-inspired background elements (digital patterns, abstract shapes, network grids) Space for an optional tagline or slogan (e.g., “Innovation. Quality. Global Impact.”) Adaptability for other platforms (so the design style can be reused for LinkedIn or Twitter headers)
Should not have
• Cluttered or overloaded layouts that reduce clarity Low-quality stock photos or generic imagery that doesn’t fit a premium brand Use of colors outside the Velbrook brand identity (Neon Green & Deep Blue) Outdated design styles (e.g., heavy gradients, 3D effects, drop shadows) Complex text blocks that make the design look busy Elements that distract from the logo and core brand message Pop-art or playful styles that don’t match the premium, professional tech look

```html
<!DOCTYPE html>
<html lang="en">
<head>
<meta charset="UTF-8">
<title>Velbrook Systems – Cover &amp; Profile</title>
<link href="https://fonts.googleapis.com/css2?family=Montserrat:wght@700&display=swap" rel="stylesheet">
<style>
  :root {
    --neon-green: #33ea33;
    --mid-teal: #1aa39a;
    --deep-blue: #0a64ea;
    --white: #ffffff;
    --ink: #1c2230;
  }
  html, body {
    margin: 0;
    padding: 0;
    width: 1200px;
    height: 660px;
    overflow: hidden;
    background: var(--white);
  }
  .canvas {
    position: relative;
    width: 1200px;
    height: 660px;
    background: var(--white);
    font-family: "Montserrat", "Helvetica Neue", Arial, sans-serif;
  }
  .cover-band {
    position: absolute;
    left: 72px;
    top: 74px;
    width: 1056px;
    height: 400px;
    background: linear-gradient(90deg, var(--neon-green) 0%, var(--mid-teal) 50%, var(--deep-blue) 88%, var(--deep-blue) 100%);
    border: 1px solid var(--deep-blue);
    box-sizing: border-box;
  }
  .headline {
    position: absolute;
    left: 72px;
    top: 214px;
    width: 1056px;
    margin: 0;
    text-align: center;
    color: var(--white);
    font-weight: 700;
    font-size: 43px;
    line-height: 57px;
    letter-spacing: 0.2px;
  }
  .profile-badge {
    position: absolute;
    left: 146px;
    top: 388px;
    width: 232px;
    height: 232px;
    border-radius: 50%;
    background:
      linear-gradient(var(--white), var(--white)) padding-box,
      linear-gradient(135deg, var(--neon-green), var(--deep-blue)) border-box;
    border: 1.5px solid transparent;
    box-sizing: border-box;
    display: flex;
    flex-direction: column;
    align-items: center;
    justify-content: center;
  }
  .brand-dot {
    width: 40px;
    height: 40px;
    border-radius: 50%;
    background: var(--deep-blue);
    margin-bottom: 18px;
  }
  .brand-name {
    margin: 0;
    color: var(--ink);
    font-weight: 700;
    text-align: center;
    font-size: 27px;
    line-height: 30px;
    letter-spacing: 1px;
  }
  .brand-name .brand-suffix {
    display: block;
    font-size: 15px;
    line-height: 22px;
    letter-spacing: 0.3px;
  }
</style>
</head>
<body>
  <main class="canvas">
    <section class="cover-band"></section>
    <h1 class="headline">Empowering Technology<br>Enabling Success</h1>
    <div class="profile-badge">
      <span class="brand-dot"></span>
      <p class="brand-name">VELBROOK<span class="brand-suffix">Systems GmbH</span></p>
    </div>
  </main>
</body>
</html>
```